Top header for website

Header for website Size is 1000px x 120px
I have CS5 so will need the source files photoshop, illustrator etc, so I can change text and photos.
Photos attached, includes example header and screenshot of eg site
Brief:
I need a website header for golfers where I can change the photos and their name.
The header needs to have these things.
- pictures of the golfer (use from pics attached)
- Their name
- Also under there name is smaller text I need a line of text you can just say "Offical Website" in your e.g to me
so for example you should have
Dale Fenwick
Offical Website
And some photos that are blended with some nice golf background or some grass or other ideas that you come up with that will look better than mine I'm sure :)
Size is 1000px x 120px
It needs to look professional and blend in nicely. I don't mind how many photos are used maybe 1-4?
The text needs to look professional too but not boring.
The header you create will be used on a website for a Professional Golfer (tour pro) their job is golf, their website needs to showcase them and promote them as best as possible.
As I said above I will need to swap photos easily and edit the text so will need the source files.
So a important point here. I guess there is no need to blend or do anything to the photos you add as I will actually need to change the photos and just need a simple template that I can swap photos and edit their name.
Ultimately I would like 3 versions of the header done and source files for all 3 so I can give them(the golfers) a choice of header type.
See how you go.
Remember that the header must have the ability for me to easily swap images and of course change the text.
My goal is to use the same header for each golfer but obviously with their images and their name.
I have CS5 so will need the source files photoshop, illustrator etc
2 example headers are attached to show you my attempts :) Please do something better.
I don't want any flash.

```html
<!DOCTYPE html>
<html lang="en">
<head>
<meta charset="utf-8">
<title>Dale Fenwick – Official Website Header</title>
<link href="https://fonts.googleapis.com/css2?family=Oswald:wght@700&family=Open+Sans:ital,wght@1,400&display=swap" rel="stylesheet">
<style>
  :root {
    --sky-top: #dfe9d8;
    --sky-haze: #c9dcb4;
    --treeline: #6f9a45;
    --grass-light: #5f9b2c;
    --grass-dark: #2f5d12;
    --portrait-light: #7f9a6a;
    --portrait-dark: #33472a;
    --frame-white: #ffffff;
    --name-gold-top: #fff36a;
    --name-gold-bottom: #f4a80c;
    --name-edge: #5a3a05;
    --tagline: #ffffff;
  }
  html, body {
    margin: 0;
    padding: 0;
    overflow: hidden;
    background: #ffffff;
  }
  .site-header {
    position: relative;
    width: 1200px;
    height: 144px;
    overflow: hidden;
  }
  .course-scene {
    position: absolute;
    inset: 0;
    background:
      radial-gradient(ellipse 260px 110px at 1075px 70px, rgba(255,255,255,0.55), transparent 70%),
      linear-gradient(180deg, var(--sky-top) 0%, var(--sky-haze) 22%, var(--treeline) 34%, var(--grass-light) 55%, var(--grass-dark) 100%);
  }
  .header-shapes {
    position: absolute;
    inset: 0;
  }
  .golfer-name {
    position: absolute;
    left: 405px;
    top: 16px;
    width: 346px;
    text-align: center;
    margin: 0;
  }
  .golfer-name__title {
    display: block;
    font-family: "Oswald", "Arial Narrow", sans-serif;
    font-weight: 700;
    font-size: 60px;
    line-height: 66px;
    letter-spacing: 0.5px;
    background: linear-gradient(180deg, var(--name-gold-top) 15%, var(--name-gold-bottom) 85%);
    -webkit-background-clip: text;
    background-clip: text;
    color: transparent;
    -webkit-text-stroke: 1px var(--name-edge);
    filter: drop-shadow(1px 2px 2px rgba(0,0,0,0.55));
  }
  .golfer-name__tagline {
    position: absolute;
    left: 537px;
    top: 84px;
    margin: 0;
    font-family: "Open Sans", Arial, sans-serif;
    font-style: italic;
    font-weight: 400;
    font-size: 27px;
    line-height: 34px;
    color: var(--tagline);
    text-shadow: 1px 1px 3px rgba(0,0,0,0.6);
  }
</style>
</head>
<body>
  <header class="site-header">
    <div class="course-scene" role="img" aria-label="Golf course fairway with a driver head and a ball on a tee"></div>
    <svg class="header-shapes" width="1200" height="144" viewBox="0 0 1200 144">
      <defs>
        <linearGradient id="portraitFill" x1="0" y1="0" x2="1" y2="1">
          <stop offset="0" stop-color="var(--portrait-light)"/>
          <stop offset="1" stop-color="var(--portrait-dark)"/>
        </linearGradient>
      </defs>
      <path class="portrait-area" role="img" aria-label="Portrait photo of the golfer"
            d="M0 0 H384 Q400 72 380 144 H0 Z" fill="url(#portraitFill)"/>
      <path class="portrait-frame" d="M384 0 Q400 72 380 144"
            fill="none" stroke="var(--frame-white)" stroke-width="7"/>
    </svg>
    <h1 class="golfer-name"><span class="golfer-name__title">Dale Fenwick</span></h1>
    <p class="golfer-name__tagline">Offical Website</p>
  </header>
</body>
</html>
```